One name card with 4 companies logos

Hi, I would like to have a design of name card with my 4 companies logos incorporated into a single, 2-sided name card.

Information for name card:
1. Slogan "Transforming Lives"
2. Critical info: "Name", "Role", "Mobile Number", "Email", "Website"
3. Please follow the sequence in placing the logos (DVX, KRPE, Brivoquest, Nevo Foundation)

Page 1 of namecard - 4 Company Logos
Page 2 of namecard - Transforming Lives + Namecard information

B2B - Companies and government bodies

4. Please put this in the page 2 of card:
Accredited Training Provider
(7 logos/icons of different brands)

Designer to choose colors to be used in the design.

• Use white as a base color for namecard

```html
<!DOCTYPE html>
<html lang="en">
<head>
<meta charset="utf-8">
<title>Name Card – Transforming Lives</title>
<link rel="stylesheet" href="https://fonts.googleapis.com/css2?family=Open+Sans:wght@400;600;700&family=Michroma&display=swap">
<style>
  :root {
    --backdrop: #858585;
    --card-light: #ebebeb;
    --card-dark: #2a2a2a;
    --ink: #1d1d1d;
    --ink-soft: #333333;
    --silver: #e2e2e2;
    --dvx-gold: #c4992c;
    --krpe-black: #111111;
    --brivo-blue: #1f3f99;
    --nevo-green: #4fb43a;
  }
  html, body {
    margin: 0;
    padding: 0;
    width: 1200px;
    height: 900px;
    overflow: hidden;
    background: var(--backdrop);
    font-family: "Open Sans", Arial, sans-serif;
  }
  .stage {
    position: relative;
    width: 1200px;
    height: 900px;
  }
  .card {
    position: absolute;
    top: 306px;
    width: 439px;
    height: 271px;
    border-radius: 12px;
    overflow: hidden;
  }
  .card--info {
    left: 149px;
    background: var(--card-light);
  }
  .card--slogan {
    left: 609px;
    background: var(--card-dark);
  }
  .brand-list {
    position: absolute;
    left: 0;
    top: 0;
    width: 200px;
    height: 100%;
  }
  .brand {
    position: absolute;
    left: 0;
    width: 200px;
    text-align: center;
    font-weight: 700;
    white-space: nowrap;
    display: flex;
    align-items: center;
    justify-content: center;
    gap: 6px;
  }
  .brand__dot {
    display: inline-block;
    width: 14px;
    height: 14px;
    border-radius: 50%;
  }
  .brand--dvx { top: 24px; font-size: 21px; color: var(--dvx-gold); letter-spacing: 1px; }
  .brand--krpe { top: 75px; font-size: 17px; color: var(--krpe-black); }
  .brand--krpe .brand__dot { background: var(--krpe-black); }
  .brand--brivo { top: 148px; font-size: 14px; color: var(--brivo-blue); }
  .brand--nevo { top: 233px; font-size: 12px; font-weight: 600; color: var(--nevo-green); }
  .brand--nevo .brand__dot { background: var(--nevo-green); }
  .contact {
    position: absolute;
    left: 229px;
    top: 73px;
    color: var(--ink);
  }
  .contact__name {
    margin: 0;
    font-size: 16px;
    font-weight: 700;
    line-height: 22px;
  }
  .contact__role {
    margin: 0;
    font-size: 12px;
    line-height: 16px;
    color: var(--ink-soft);
  }
  .contact__lines {
    list-style: none;
    margin: 41px 0 0;
    padding: 0;
    font-size: 12px;
    line-height: 18px;
    color: var(--ink-soft);
  }
  .contact__lines li {
    display: flex;
    align-items: center;
    gap: 7px;
  }
  .contact__icon {
    width: 9px;
    height: 9px;
    fill: var(--ink);
  }
  .slogan {
    position: absolute;
    left: 0;
    top: 0;
    width: 439px;
    height: 271px;
  }
  .slogan text {
    font-family: "Michroma", "Arial Black", sans-serif;
    fill: var(--silver);
  }
</style>
</head>
<body>
<main class="stage">
  <section class="card card--info" aria-label="Card front with company names and contact details">
    <div class="brand-list">
      <div class="brand brand--dvx">DVX</div>
      <div class="brand brand--krpe"><span class="brand__dot"></span>KRPE</div>
      <div class="brand brand--brivo">Brivoquest.com</div>
      <div class="brand brand--nevo"><span class="brand__dot"></span>NEVO FOUNDATION</div>
    </div>
    <div class="contact">
      <h1 class="contact__name">Marcus Ellery</h1>
      <p class="contact__role">Managing Director</p>
      <ul class="contact__lines">
        <li>
          <svg class="contact__icon" viewBox="0 0 10 10" aria-hidden="true"><path d="M2 0.5 L3.6 2.6 L2.7 3.6 Q3.8 5.8 6.4 7.3 L7.4 6.4 L9.5 8 L8.3 9.5 Q4.5 9.2 0.5 1.7 Z"/></svg>
          (055)-218-3046
        </li>
        <li>
          <svg class="contact__icon" viewBox="0 0 10 10" aria-hidden="true"><path d="M0.5 2 H9.5 V8 H0.5 Z M1.2 2.6 L5 5.3 L8.8 2.6 V3.3 L5 6 L1.2 3.3 Z" fill-rule="evenodd"/></svg>
          hello@ellerymail.com
        </li>
        <li>
          <svg class="contact__icon" viewBox="0 0 10 10" aria-hidden="true"><circle cx="5" cy="5" r="4.5"/></svg>
          www.ellerysite.com
        </li>
      </ul>
    </div>
  </section>

  <section class="card card--slogan" aria-label="Card back with slogan">
    <svg class="slogan" viewBox="0 0 439 271" role="img" aria-label="Transforming Lives">
      <text x="47" y="106" font-size="27" textLength="341" lengthAdjust="spacingAndGlyphs">TRANSFORMING</text>
      <text x="47" y="189" font-size="86" textLength="345" lengthAdjust="spacingAndGlyphs">LIVES</text>
    </svg>
  </section>
</main>
</body>
</html>
```